Modern home page design for insurance and investment business

- The design should be based around the attached HPID (home page information design) called KRT HPID. The table boxes are just for approximate placement of information – you DON'T have to make it look exactly like this.
- Information only is in orange text. Copy to go on the design in black text. Some instructions are in the HPID. Please be creative! You don’t have to use the exact images provided if you have a better idea.

- The design needs to be clean and spacious. Please use the colours from the logos in the website design. Lots of white too.

I've attached home page gallery example photos. You can use any of these photos or something similar with the words from one of the photos.

- Expected standard of design examples: (Please DO NOT copy these exactly – they are just examples)
http://www.brackenvale.example.nz/
https://www.tarnwick.example.nz/
http://quillmoorcover.example.nz/homepage/

Width of content will be 1100 pixels when implemented as a web page. Header height (without nav bar) 150-160 pixels.

The winning PSD file will have to be provided as follows…
1. Canvas size of 2000px x 2000px - 72ppi in Adobe Photoshop (CS5 compatible)
2. Width of content section is 1100px wide - centered in the canvas
3. Any button rollovers/hovers in the PSD as hidden layers.
4. All fonts used must be Google fonts (except for the fonts in the header at the top of the page).
5. You will need to supply the chosen home page plus one example page (example page as a style guide for how all other pages will look). Example page is only the header and navigational bar at the top, an empty sector in the middle with a column (180 px wide) which can be left or right aligned which means the main sector is 920 pixels wide, and then the footer at the bottom of the page.

```html
<!DOCTYPE html>
<html lang="en">
<head>
<meta charset="utf-8">
<title>KRT Insure &amp; Invest</title>
<link href="https://fonts.googleapis.com/css2?family=Roboto:ital,wght@0,400;0,500;0,700;1,400&family=Lato:wght@400&family=Noticia+Text:ital,wght@1,700&display=swap" rel="stylesheet">
<style>
:root{
  --navy:#003a70;
  --navy-dark:#002d58;
  --slate:#8d9aa7;
  --grey-text:#9a9a9a;
  --body-text:#3a3a3a;
  --footer-dark:#2b2b2b;
  --white:#ffffff;
}
*{box-sizing:border-box;margin:0;padding:0}
html,body{width:1061px;height:1200px;overflow:hidden}
body{position:relative;font-family:'Roboto',sans-serif;background:var(--white);color:var(--body-text)}
.abs{position:absolute}

.header{left:0;top:0;width:1061px;height:130px;background:linear-gradient(#e6e6e6,#f7f7f7)}
.brand{left:104px;top:46px;display:flex;align-items:center;gap:10px;font-size:30px;font-weight:700;color:var(--navy);letter-spacing:.5px}
.brand-dot{width:26px;height:26px;border-radius:50%;background:var(--navy)}
.brand-sub{left:140px;top:84px;font-size:13px;font-weight:700;color:var(--navy);letter-spacing:.3px}
.locator{left:385px;top:19px;width:248px;height:93px;border:1px solid #c9c9c9;background:#eeeae2}
.locator-title{height:27px;background:#9ea3a8;color:var(--white);font-size:13px;line-height:27px;padding-left:10px}
.locator-map{height:64px;background:linear-gradient(135deg,#ece8df,#e2ddd2 60%,#cfe3c4)}
.locator-tag{left:99px;top:35px;width:106px;background:var(--white);border:1px solid #ccc;font-size:11px;line-height:13px;text-align:center;padding:2px 0;color:#333}
.tagline{right:105px;top:37px;font-size:12px;font-weight:700;color:var(--navy)}
.services{right:105px;top:58px;font-size:12px;font-weight:500;color:var(--grey-text)}
.phones{right:105px;top:79px;display:flex;align-items:center;gap:5px;font-size:15px;font-weight:500;color:var(--navy)}

.nav{left:0;top:130px;width:1061px;height:37px;background:var(--navy)}
.nav a{position:absolute;top:0;height:37px;line-height:37px;text-align:center;color:var(--white);font-size:13px;text-decoration:none;border-left:1px solid var(--navy-dark)}
.nav a.active{background:var(--slate)}

.hero{left:0;top:167px;width:1061px;height:383px;background:linear-gradient(#8a6a33 0%,#c49a55 30%,#a98245 52%,#3a2a14 68%,#050505 78%,#000 100%)}
.hero-title{left:104px;top:62px;font-family:'Noticia Text',serif;font-style:italic;font-weight:700;font-size:29px;color:var(--white)}
.hero-arrow{top:177px}

.about{left:104px;top:550px;width:852px;height:210px;background:var(--white)}
.about h2{position:absolute;left:6px;top:10px;font-size:17px;font-weight:700;color:var(--navy)}
.about-rule{left:6px;top:33px;width:533px;border-top:1px dashed #b8b8b8}
.about-copy{left:6px;top:40px;width:540px;font-family:'Lato',sans-serif;font-size:10px;line-height:16px;color:var(--body-text);text-align:justify}
.about-copy p+p{margin-top:7px}
.about-photo{left:575px;top:35px;width:270px;height:146px;border:1px solid #c9c9c9;padding:4px;background:var(--white)}
.about-photo div{width:100%;height:100%;background:linear-gradient(160deg,#9cc07a,#6e9a4c 45%,#a7c5dd 70%,#5e88b8)}

.callback{left:0;top:760px;width:1061px;height:226px;background:linear-gradient(var(--white),#e2e2e2 40%,#e2e2e2)}
.callback-rule{left:139px;top:-1px;width:800px;border-top:1px solid #c7c7c7}
.callback h3{position:absolute;left:0;width:1061px;top:14px;text-align:center;font-size:17px;font-weight:700;color:var(--navy)}
.field{position:absolute;background:var(--white);border:1px solid #d5d5d5;border-radius:3px;font-size:11px;font-style:italic;color:#333;padding:9px 11px}
.send{left:846px;top:167px;width:93px;height:31px;background:var(--navy);border-radius:3px;color:var(--white);font-size:15px;font-weight:700;text-align:center;line-height:31px}

.foot-band{left:0;top:986px;width:1061px;height:37px;background:var(--navy)}
.foot-band h4{position:absolute;top:0;line-height:37px;font-size:13px;font-weight:500;color:var(--white)}
.foot{left:0;top:1023px;width:1061px;height:177px;background:var(--footer-dark);color:var(--white);font-size:10px}
.foot ul{list-style:none;position:absolute}
.quick li{line-height:15.5px}
.stages li{width:137px;height:29px;line-height:20px;border-bottom:1px solid #666}
.stages li:last-child{border:0}
.prod-head{font-weight:700}
.prod li{line-height:13.5px}
.foot-map{left:698px;top:13px;width:110px;height:100px;background:linear-gradient(135deg,#e8e5dd,#ddd8cc);border:1px solid #888}
.contact-row{position:absolute;left:814px;display:flex;gap:4px;line-height:12.5px}
.copyline{left:104px;top:132px;width:852px;border-top:1px solid #555}
.copy{left:106px;top:147px;font-weight:700}
.social{left:882px;top:143px;display:flex;align-items:center;gap:6px;font-weight:500}
.social-sq{width:15px;height:15px;background:var(--white)}
</style>
</head>
<body>

<header class="header abs">
  <div class="brand abs"><span class="brand-dot"></span>KRT</div>
  <div class="brand-sub abs">INSURE &amp; INVEST</div>
  <div class="locator abs">
    <div class="locator-title">Servicing Clients New Zealand Wide</div>
    <div class="locator-map" role="img" aria-label="Street map of Gisborne"></div>
    <div class="locator-tag abs">Located in sunny<br>Gisborne</div>
  </div>
  <div class="tagline abs">Smart Financial Decisions For Today And For Your Future</div>
  <div class="services abs">Insurances &nbsp;/&nbsp; Investments &nbsp;/&nbsp; Financial Planning</div>
  <div class="phones abs">
    <svg width="16" height="16" viewBox="0 0 16 16"><circle cx="8" cy="8" r="7" fill="none" stroke="#003a70" stroke-width="1.3"/><path d="M6 4.5c-1 .6-1.3 2.3-.3 4.3s2.6 3 3.6 2.8l.8-1.3-1.5-1-.7.6c-.7-.3-1.4-1.2-1.6-2l.7-.5-.6-1.7z" fill="#003a70"/></svg>
    0800 552 4170 &nbsp;|&nbsp; 06 552 4170
  </div>
</header>

<nav class="nav abs">
  <a style="left:108px;width:62px">Home</a>
  <a class="active" style="left:170px;width:64px">About</a>
  <a style="left:234px;width:99px">What We Do</a>
  <a style="left:333px;width:167px">What Life Stage are You?</a>
  <a style="left:500px;width:92px">Insurances</a>
  <a style="left:592px;width:99px">Investments</a>
  <a style="left:691px;width:63px">FAQs</a>
  <a style="left:754px;width:100px">Consultation</a>
  <a style="left:854px;width:102px">Contact/Map</a>
</nav>

<section class="hero abs" role="img" aria-label="Tractor silhouetted against a golden sunset sky">
  <div class="hero-title abs">Planning for a Rainy day...</div>
  <svg class="hero-arrow abs" style="left:86px" width="16" height="26" viewBox="0 0 16 26"><path d="M13 2 3 13l10 11" fill="none" stroke="#3a3a3a" stroke-width="3"/></svg>
  <svg class="hero-arrow abs" style="left:958px" width="16" height="26" viewBox="0 0 16 26"><path d="M3 2l10 11L3 24" fill="none" stroke="#3a3a3a" stroke-width="3"/></svg>
</section>

<section class="about abs">
  <h2>About us</h2>
  <div class="about-rule abs"></div>
  <div class="about-copy abs">
    <p>Lorem ipsum dolor sit amet, consectetuer adipiscing elit, sed diam nonummy nibh euismod tincidunt ut laoreet dolore magna aliquam erat volutpat. Ut wisi enim ad minim veniam, quis nostrud exerci tation ullamcorper suscipit lobortis nisl ut aliquip ex ea commodo consequat. Duis autem vel eum iriure dolor in hendrerit in vulputate velit esse molestie consequat, vel illum dolore eu feugiat nulla facilisis at vero eros et accumsan et iusto odio dignissim qui blandit</p>
    <p>Lorem ipsum dolor sit amet, consectetuer adipiscing elit, sed diam nonummy nibh euismod tincidunt ut laoreet dolore magna aliquam erat volutpat. Ut wisi enim ad minim veniam, quis nostrud exerci tation ullamcorper suscipit lobortis Lorem ipsum dolor sit amet, consectetuer adipiscing elit, sed diam nonummy nibh euismod tincidunt ut laoreet dolore magna aliquam erat volutpat. Ut wisi enim ad minim veniam, quis nostrud exerci tation ullamcorper suscipit lobortis</p>
  </div>
  <div class="about-photo abs"><div role="img" aria-label="Smiling family outdoors on a green lawn"></div></div>
</section>

<section class="callback abs">
  <div class="callback-rule abs"></div>
  <h3>Would You Like KRT To Call You? Fill In The Form And We’ll Be In Touch...</h3>
  <div class="field" style="left:122px;top:51px;width:401px;height:31px">First Name:</div>
  <div class="field" style="left:122px;top:90px;width:401px;height:31px">Last Name:</div>
  <div class="field" style="left:122px;top:128px;width:401px;height:31px">Email:</div>
  <div class="field" style="left:122px;top:167px;width:401px;height:31px">Phone:</div>
  <div class="field" style="left:538px;top:51px;width:401px;height:107px">Message:</div>
  <div class="send abs">SEND</div>
</section>

<div class="foot-band abs">
  <h4 style="left:104px">Quick Links</h4>
  <h4 style="left:273px">What Life Stage Are You?</h4>
  <h4 style="left:463px">Products/Services</h4>
  <h4 style="left:698px">Contact/Map</h4>
</div>

<footer class="foot abs">
  <ul class="quick" style="left:106px;top:10px">
    <li>Home</li><li>About</li><li>&gt; Meet the Team</li><li>&gt; Testimonials</li><li>What We Do</li><li>FAQs</li><li>Consultation</li>
  </ul>
  <ul class="stages" style="left:272px;top:6px">
    <li>Life stage 18-30 years</li><li>Life stage 30-45 years</li><li>Life stage 45-65 years</li><li>Life stage 65+ years</li>
  </ul>
  <div class="prod-head abs" style="left:463px;top:10px">Insurance</div>
  <ul class="prod" style="left:464px;top:27px">
    <li>&gt; Life insurance</li><li>&gt; Trauma insurance</li><li>&gt; Disablement cover</li><li>&gt; Income protection</li>
  </ul>
  <ul class="prod" style="left:565px;top:27px">
    <li>&gt; Health insurance</li><li>&gt; Business insurance</li><li>&gt; Fire &amp; General</li><li>&gt; Travel insurance</li>
  </ul>
  <div class="prod-head abs" style="left:464px;top:86px">Investment</div>
  <ul class="prod" style="left:464px;top:103px"><li>&gt; NestSaver</li></ul>

  <div class="foot-map abs" role="img" aria-label="Map showing the office location in Gisborne"></div>
  <div class="contact-row" style="top:15px">
    <svg width="14" height="18" viewBox="0 0 14 18" style="margin-left:-2px"><path d="M7 1a6 6 0 0 0-6 6c0 4.5 6 10 6 10s6-5.5 6-10a6 6 0 0 0-6-6z" fill="#fff"/><circle cx="7" cy="7" r="2.3" fill="#2b2b2b"/></svg>
    <span>48 Harlow Rd, Gisborne<br>New Zealand PO Box 4410,<br>Gisborne</span>
  </div>
  <div class="contact-row" style="top:60px">
    <svg width="14" height="14" viewBox="0 0 14 14" style="margin-left:-2px"><circle cx="7" cy="7" r="5.8" fill="none" stroke="#fff" stroke-width="1.4"/><path d="M7 3.5V7l2.3 1.5" fill="none" stroke="#fff" stroke-width="1.4"/></svg>
    <span>Office Hours: 8.30 – 5pm<br>After Hours: Please phone:</span>
  </div>
  <div class="contact-row" style="top:88px;font-weight:700">
    <svg width="14" height="14" viewBox="0 0 14 14" style="margin-left:-2px"><circle cx="7" cy="7" r="6" fill="none" stroke="#fff" stroke-width="1.3"/><path d="M5.3 3.8c-.9.5-1.1 2-.2 3.7s2.2 2.6 3.1 2.4l.7-1.1-1.3-.9-.6.5c-.6-.3-1.2-1-1.4-1.7l.6-.4-.5-1.5z" fill="#fff"/></svg>
    <span>0800 552 4170<br>06 552 4170</span>
  </div>

  <div class="copyline abs"></div>
  <div class="copy abs">© 2014 KRT Investment | All Rights Reserved.</div>
  <div class="social abs"><span class="social-sq"></span>Chatterbook</div>
</footer>

</body>
</html>
```